I want our new logo design to guide the colors and look of the home page. I want it to be vibrant and contemporary. We are a new religious education publishing company. I would like any colors used to describe the product below to be bright and cheerful, but also to look good with our logo colors
On our home page we are introducing a new product for second graders. The product name should look child friendly, but not silly. If there is a way to add reverence to the words FIRST RECONCILIATION and FIRST EUCHARIST, and still make it look like it is a product for children, that would be great.
The product will be called:
Little Pilgrim Learning Set for the Open Door Room
FIRST RECONCILIATION
FIRST EUCHARIST
THE PRODUCT DESCRIPTION SHOULD BE AS FOLLOWS
Field tested and designed for the special needs inclusive classroom
Kit includes high impact visuals, hands-on activities, manipulatives, games, and other teaching aids for total engagement of ALL students
Detailed catechist lesson plans to maximize learning and retention
Cost effective reusable kit
Bilingual
Somewhere it should say COMING SOON, because the product is not ready yet, but we are promoting it. I don't have a picture of this product yet, but above the product description, we need an empty box that we'll use when we're ready to upload the picture of the kit.
There should also be a statement near the product description that says: To learn more about the Little Pilgrim Set for the Open Door Room, click here.
Web page links:
About Us
Products
Resources
Contact Us
I would also like a few links to be featured on the home page:
Faith Lessons for Tomorrow's Hearts....learn more
"Where Do We Begin?"....learn more
Could It Be Something Deeper Inside?...learn more
The Dream and the Daily...learn more
Genuine Welcoming Formation
I have increased my budget and clarified my brief so that it's easier to understand. It's basically just a home page and a template for the other pages. There is no content on the other web pages that you have to work on. I just need a well designed home page and a nice template for the other pages.
Reason: I am extending the deadline for 2 days so that templates can be designed for 5 additional web pages. Please make each template a little different from the way you designed the home page. These pages can have blank picture boxes and dummy text to save you time. I am only interested in layout for the addtional pages. Thank you!
We've made a selection and wanted to thank all of you for your wonderful designs!

```html
<!DOCTYPE html>
<html lang="en">
<head>
<meta charset="utf-8">
<title>Lantern Path Catechetics</title>
<link rel="stylesheet" href="https://fonts.googleapis.com/css2?family=Nunito:wght@800;900&family=Open+Sans:wght@400;700&family=Play&family=Mulish:wght@400&display=swap">
<style>
:root{
  --header-brown:#4a3219;
  --footer-brown:#2b1f12;
  --brand-orange:#f39a12;
  --brand-red:#c8202f;
  --brand-red-dark:#7d1019;
  --paper:#efe8dc;
  --ink:#3d3d3d;
  --soft:#8b8b8b;
  --footer-text:#8d7f6b;
  --footer-head:#b2a48d;
  --white:#ffffff;
}
*{margin:0;padding:0;box-sizing:border-box}
html,body{width:999px;height:1200px;overflow:hidden;background:var(--white)}
body{position:relative;font-family:"Open Sans",Verdana,sans-serif;color:var(--ink)}
.abs{position:absolute}

.site-header{left:0;top:0;width:999px;height:163px;background:var(--header-brown)}
.brand{left:0;top:74px;width:999px;display:flex;flex-direction:column;align-items:center}
.brand-row{display:flex;align-items:center;gap:10px}
.brand-dot{width:20px;height:20px;border-radius:50%;background:var(--brand-orange)}
.brand-name{font-family:"Mulish",sans-serif;font-size:29px;color:var(--brand-orange);letter-spacing:.2px}
.brand-tag{font-family:"Mulish",sans-serif;font-size:16px;color:#b9a88f;margin-top:4px;margin-left:58px}

.main-nav{left:0;top:163px;width:999px;height:79px;background:var(--white)}
.main-nav ul{list-style:none;position:absolute;left:181px;top:25px;display:flex}
.main-nav li{font-family:"Mulish",sans-serif;font-size:19px;color:#3a2a18;margin-right:29px;padding-bottom:6px}
.main-nav li.current{border-bottom:2px solid var(--brand-red)}
.main-nav li:nth-child(3){margin-right:34px}

.stage{left:0;top:242px;width:999px;height:515px;background:var(--paper)}

.feature{left:61px;top:245px;width:875px;height:494px;background:#fbf9f5;box-shadow:0 3px 6px rgba(0,0,0,.35)}
.feature-bar{left:0;top:0;width:875px;height:57px;background:var(--brand-orange)}
.feature-bar h2{font-family:"Play",sans-serif;font-weight:400;font-size:32px;color:#4a3219;position:absolute;left:18px;top:8px;letter-spacing:.4px;white-space:nowrap}
.kit-photo{left:9px;top:99px;width:236px;height:268px;border-radius:4px;background:radial-gradient(circle at 50% 45%,#f6c84a 0%,#e8567a 35%,#5aa7d8 65%,#f4f1ea 90%)}

.ribbon{left:-9px;top:377px;width:290px;height:50px}
.ribbon svg{position:absolute;left:0;top:0}
.ribbon span{position:absolute;left:0;top:0;width:262px;height:38px;display:flex;align-items:center;justify-content:center;font-family:"Nunito",sans-serif;font-weight:900;font-size:22px;color:var(--white);white-space:nowrap}

.headline{left:303px;top:90px;font-family:"Nunito",sans-serif;font-weight:900;font-size:53px;line-height:56px;color:var(--brand-orange);letter-spacing:1.2px;white-space:nowrap}
.features{left:311px;top:216px;width:470px;list-style:none}
.features li{position:relative;padding-left:13px;font-size:18.5px;line-height:18.5px;color:#4b4b4b;margin-bottom:7px}
.features li::before{content:"";position:absolute;left:0;top:6px;width:7px;height:7px;border-radius:50%;background:#6a6a6a}

.btn{top:438px;height:42px;border-radius:13px;background:var(--brand-orange);color:var(--white);font-family:"Nunito",sans-serif;font-weight:900;display:flex;align-items:center;justify-content:center;white-space:nowrap}
.btn-learn{left:305px;width:201px;font-size:23px}
.btn-notify{left:552px;width:303px;font-size:18px}

.intro{left:79px;top:780px;width:440px}
.intro h3,.links h3{font-size:16.5px;font-weight:700;color:#6b6b6b;margin-bottom:10px}
.intro p{font-size:13.6px;line-height:16px;color:var(--soft)}
.intro b,.links b{color:#6b6b6b}
.col-rule{left:563px;top:803px;height:165px;border-left:1px dotted #bdbdbd}
.links{left:581px;top:780px;width:360px}
.links ul{list-style:none}
.links li{font-size:13.6px;line-height:19px;color:var(--soft);white-space:nowrap}

.site-footer{left:0;top:1038px;width:999px;height:162px;background:var(--footer-brown)}
.site-footer h4{font-size:19px;font-weight:700;color:var(--footer-head);letter-spacing:.5px;margin-bottom:10px}
.foot-contact{left:60px;top:20px}
.foot-contact p{font-size:13.6px;line-height:19px;color:var(--footer-text)}
.foot-rule{top:22px;height:125px;border-left:1px dotted #6b5d4a}
.foot-rule-a{left:297px}
.foot-rule-b{left:806px}
.foot-site{left:322px;top:20px;width:460px}
.foot-site p{font-size:13.6px;line-height:23px;color:var(--footer-text)}
.foot-site .copy{margin-top:10px}
.foot-find{left:833px;top:20px}
.social{display:flex;gap:12px;margin-top:4px}
.social span{width:28px;height:28px;border-radius:3px}
.social .s1{background:#3b5a98}
.social .s2{background:#3fb8e6}
</style>
</head>
<body>

<header class="site-header abs">
  <div class="brand abs">
    <div class="brand-row">
      <span class="brand-dot"></span>
      <span class="brand-name">Lantern Path Catechetics</span>
    </div>
    <div class="brand-tag">a new approach to catechesis</div>
  </div>
</header>

<nav class="main-nav abs">
  <ul>
    <li class="current">HOME</li>
    <li>ABOUT US</li>
    <li>PRODUCTS</li>
    <li>RESOURCES</li>
    <li>CONTACT US</li>
  </ul>
</nav>

<div class="stage abs"></div>

<section class="feature abs">
  <div class="feature-bar abs"><h2>Little Pilgrim Learning Set for the Open Door Room</h2></div>
  <div class="kit-photo abs" role="img" aria-label="Product image area: colourful painted child's handprint"></div>

  <div class="ribbon abs">
    <svg width="290" height="50" viewBox="0 0 290 50">
      <polygon points="0,0 288,0 260,19 288,38 0,38" fill="#c8202f"/>
      <polygon points="0,38 10,38 10,49" fill="#7d1019"/>
    </svg>
    <span>Coming soon!</span>
  </div>

  <div class="headline abs">First Reconciliation<br>First Eucharist</div>

  <ul class="features abs">
    <li>Field tested and designed for the special needs inclusive classroom</li>
    <li>Kit includes high impact visuals, hands-on activities, manipulatives, games, and other teaching aids for total engagement of ALL students</li>
    <li>Detailed catechist lesson plans to maximize learning and retention</li>
    <li>Cost effective reusable kit</li>
    <li>Bilingual</li>
  </ul>

  <div class="btn btn-learn abs">Learn more</div>
  <div class="btn btn-notify abs">E-mail me when available</div>
</section>

<section class="intro abs">
  <h3>A new approach to catechesis</h3>
  <p>There are many variations of passages of Lorem Ipsum available, but the majority have suffered alteration in some form, by injected humour, or randomised words which don't look even slightly believable. If you are going to use a passage of Lorem Ipsum, you need to be sure there isn't anything embarrassing hidden in the middle of text. All the Lorem Ipsum generators on the Internet tend to repeat predefined chunks as necessary, making this the first true generator on the Internet. It uses a dictionary of over 200 Latin words, combined with a handful of model sentence structures, to generate Lorem Ipsum which looks reasonable. The generated Lorem Ipsum is therefore always free from repetition, injected humour, or non-characteristic words etc. <b>Read more...</b></p>
</section>

<div class="col-rule abs"></div>

<section class="links abs">
  <h3>Another heading</h3>
  <ul>
    <li>Faith Lessons for Tomorrow's Hearts. <b>Learn more...</b></li>
    <li>"Where Do We Begin?" <b>Learn more...</b></li>
    <li>Could It Be Something Deeper Inside? <b>Learn more...</b></li>
    <li>The Dream and the Daily. <b>Learn more...</b></li>
    <li>Genuine Welcoming Formation. <b>Learn more...</b></li>
  </ul>
</section>

<footer class="site-footer abs">
  <div class="foot-contact abs">
    <h4>CONTACT</h4>
    <p>12 Harbour Lane<br>Brightwater NSW 2099<br>555.012.347<br>hello@lanternpath.example</p>
  </div>
  <div class="foot-rule foot-rule-a abs"></div>
  <div class="foot-site abs">
    <h4>LANTERN PATH CATECHETICS</h4>
    <p>HOME &nbsp;| &nbsp;ABOUT US &nbsp;| &nbsp;PRODUCTS &nbsp;| &nbsp;RESOURCES &nbsp;| CONTACT US<br>PRIVACY &nbsp;| &nbsp;SITE MAP</p>
    <p class="copy">© 2011 Lantern Path Catechetics</p>
  </div>
  <div class="foot-rule foot-rule-b abs"></div>
  <div class="foot-find abs">
    <h4>FIND US</h4>
    <div class="social"><span class="s1"></span><span class="s2"></span></div>
  </div>
</footer>

</body>
</html>
```